Smartphone speedcam App design

We are Dubai based company named QWRN. We are looking design for our Android app. We developed Speed Camera intimation Android app. Our application required GPS/3G to run. The idea is to control over speeding and intimate users the speed camera nearby you.
You can use app while driving. App will intimate you if you crossed road speed limit. App also intimate when speed camera nearby you. For example, Speed camera after 500 meters , 400 meters...etc.

Target Market(s)

UAE market

Industry/Entity Type

It Company

Number of Pages Required

2 page

Requirements
Must have
• my app has option to intimate for speed camera. camera icon/image can appear while intimation only rest of design can show road speed and current driving speed.
• I have attached sample main screen for designer understanding.
Nice to have
• designers can search related apps

```html
<!DOCTYPE html>
<html lang="en">
<head>
<meta charset="utf-8">
<title>QWRN Speed Camera App – Main Screens</title>
<link rel="stylesheet" href="https://fonts.googleapis.com/css2?family=Roboto:wght@300;400;500&display=swap">
<style>
  :root {
    --page-bg: #e4e4e4;
    --screen-top: #1d2d33;
    --screen-mid: #1b2a28;
    --screen-low: #18261c;
    --status-dark: #17252a;
    --status-alert: #8e2727;
    --alert-red: #e03a3c;
    --text-main: #f4f6f5;
    --text-soft: #cfd8d4;
    --rule: rgba(220, 235, 225, 0.45);
    --ring: rgba(200, 215, 205, 0.35);
    --tick-on: #7fd63a;
    --tick-dim: rgba(120, 170, 110, 0.45);
    --speed-ok: #3e9b22;
    --speed-ok-edge: #86e04a;
    --speed-over: #b0282a;
    --pill-bg: rgba(38, 52, 52, 0.85);
    --action-bg: rgba(255, 255, 255, 0.14);
    --exit-red: #c8282b;
  }
  * { box-sizing: border-box; margin: 0; padding: 0; }
  html, body { width: 1200px; height: 1000px; overflow: hidden; }
  body {
    background: var(--page-bg);
    font-family: "Roboto", sans-serif;
    color: var(--text-main);
    position: relative;
  }

  .screen {
    position: absolute;
    top: 185px;
    width: 344px;
    height: 610px;
    overflow: hidden;
  }
  .screen--normal { left: 228px; }
  .screen--alert { left: 646px; }

  .screen__backdrop {
    position: absolute; inset: 0;
    background: linear-gradient(180deg, var(--screen-top) 0%, var(--screen-mid) 45%, #1f3326 70%, var(--screen-low) 100%);
  }
  .screen__alert-glow {
    position: absolute; left: 0; right: 0; top: 0; height: 150px;
    background: linear-gradient(180deg, var(--alert-red) 0%, rgba(224, 58, 60, 0.75) 35%, rgba(224, 58, 60, 0) 100%);
  }
  .status-bar { position: absolute; left: 0; right: 0; top: 0; height: 25px; background: var(--status-dark); }
  .screen--alert .status-bar { background: var(--status-alert); }

  .location { position: absolute; left: 28px; top: 34px; }
  .location__pin { position: absolute; left: 0; top: 4px; width: 14px; height: 20px; }
  .location__road { position: absolute; left: 29px; top: 0; font-size: 16px; font-weight: 400; white-space: nowrap; }
  .location__community { position: absolute; left: 30px; top: 25px; font-size: 10px; font-weight: 500; white-space: nowrap; }

  .limits { position: absolute; left: 28px; top: 84px; width: 300px; height: 44px; }
  .limit { position: absolute; top: 0; display: flex; align-items: baseline; gap: 8px; }
  .limit--speed { left: 0; }
  .limit--camera { left: 170px; }
  .limit__icon { width: 20px; height: 20px; align-self: center; margin-right: 3px; }
  .limit__value { font-size: 37px; font-weight: 300; line-height: 1; }
  .limit__unit { font-size: 18px; font-weight: 300; }

  .rule { position: absolute; left: 24px; width: 297px; height: 1px; background: var(--rule); }
  .rule--top { top: 137px; }
  .rule--bottom { top: 495px; }

  .gauge { position: absolute; left: 42px; top: 182px; width: 260px; height: 260px; }
  .gauge__readout {
    position: absolute; left: 127px; top: 268px; width: 90px; height: 90px; border-radius: 50%;
    display: flex; flex-direction: column; align-items: center; justify-content: center;
    border: 2px solid var(--speed-ok-edge);
  }
  .screen--normal .gauge__readout { background: var(--speed-ok); }
  .screen--alert .gauge__readout { background: var(--speed-over); }
  .gauge__value { font-size: 34px; font-weight: 300; line-height: 1; margin-top: 4px; }
  .gauge__unit { font-size: 11px; margin-top: 2px; }
  .screen--normal .gauge__unit { color: #a9ec7c; }
  .screen--alert .gauge__unit { color: #ff9b9b; }

  .current-speed {
    position: absolute; left: 99px; top: 412px; width: 147px; height: 23px; border-radius: 12px;
    background: var(--pill-bg); font-size: 11px; text-align: center; line-height: 23px;
  }

  .actions { position: absolute; left: 0; top: 526px; width: 344px; }
  .action { position: absolute; top: 0; width: 90px; margin-left: -45px; text-align: center; }
  .action__icon {
    width: 30px; height: 30px; border-radius: 50%; margin: 0 auto; background: var(--action-bg);
    display: flex; align-items: center; justify-content: center;
  }
  .action__icon svg { width: 16px; height: 16px; }
  .action--exit .action__icon { background: var(--exit-red); }
  .action__label { display: block; margin-top: 15px; font-size: 9px; color: var(--text-soft); white-space: nowrap; }
  .action--school { left: 59px; }
  .action--report { left: 142px; }
  .action--settings { left: 225px; }
  .action--exit { left: 302px; }
</style>
</head>
<body>

<!-- Screen 1: within the limit -->
<section class="screen screen--normal">
  <div class="screen__backdrop" role="img" aria-label="Misty green mountain landscape at dusk"></div>
  <div class="status-bar"></div>

  <div class="location">
    <svg class="location__pin" viewBox="0 0 14 20"><path d="M7 0a7 7 0 0 1 7 7c0 5-7 13-7 13S0 12 0 7a7 7 0 0 1 7-7z" fill="#fff"/><circle cx="7" cy="7" r="2.6" fill="#1d2d33"/></svg>
    <span class="location__road">Al Noor Coastal Road</span>
    <span class="location__community">Community Name</span>
  </div>

  <div class="limits">
    <div class="limit limit--speed">
      <svg class="limit__icon" viewBox="0 0 20 20" fill="none" stroke="#fff" stroke-width="1.3"><path d="M2 15a8 8 0 1 1 16 0z"/><path d="M10 14l4-5"/></svg>
      <span class="limit__value">120</span><span class="limit__unit">Km/h</span>
    </div>
    <div class="limit limit--camera">
      <svg class="limit__icon" viewBox="0 0 20 20" fill="none" stroke="#fff" stroke-width="1.3"><rect x="3" y="2" width="14" height="9"/><circle cx="10" cy="6.5" r="2.5"/><path d="M10 11v8M10 13l-5 6M10 13l5 6"/></svg>
      <span class="limit__value">220</span><span class="limit__unit">m</span>
    </div>
  </div>
  <div class="rule rule--top"></div>

  <svg class="gauge" viewBox="0 0 260 260" fill="none">
    <path d="M43.7 216.3 A122 122 0 1 1 216.3 216.3" stroke="var(--ring)" stroke-width="1.2"/>
    <path d="M56.5 203.5 A104 104 0 1 1 234 130" stroke="var(--tick-on)" stroke-width="16" stroke-dasharray="1.4 2.3"/>
    <path d="M234 130 A104 104 0 0 1 203.5 203.5" stroke="var(--tick-dim)" stroke-width="16" stroke-dasharray="1.4 2.3"/>
    <path d="M130 130 L220 126" stroke="var(--tick-on)" stroke-width="2.4"/>
  </svg>
  <div class="gauge__readout"><span class="gauge__value">90</span><span class="gauge__unit">Km/h</span></div>
  <div class="current-speed">Current Speed</div>

  <div class="rule rule--bottom"></div>
  <nav class="actions">
    <div class="action action--school"><div class="action__icon"><svg viewBox="0 0 16 16" fill="none" stroke="#fff" stroke-width="1"><path d="M1 6l7-3 7 3-7 3z"/><path d="M4 7.5v4l4 2 4-2v-4"/></svg></div><span class="action__label">School Intimation</span></div>
    <div class="action action--report"><div class="action__icon"><svg viewBox="0 0 16 16" fill="none" stroke="#fff" stroke-width="1"><rect x="2" y="2" width="12" height="9"/><circle cx="8" cy="6.5" r="2"/><path d="M6 14h4M8 11v3"/></svg></div><span class="action__label">Report Camera</span></div>
    <div class="action action--settings"><div class="action__icon"><svg viewBox="0 0 16 16" fill="none" stroke="#fff"><circle cx="8" cy="8" r="5.5" stroke-width="2.4" stroke-dasharray="2 2.3"/><circle cx="8" cy="8" r="2.3" stroke-width="1"/></svg></div><span class="action__label">Settings</span></div>
    <div class="action action--exit"><div class="action__icon"><svg viewBox="0 0 16 16" stroke="#fff" stroke-width="1.3"><path d="M3 3l10 10M13 3L3 13"/></svg></div><span class="action__label">Exit</span></div>
  </nav>
</section>

<!-- Screen 2: over the limit -->
<section class="screen screen--alert">
  <div class="screen__backdrop" role="img" aria-label="Misty green mountain landscape at dusk"></div>
  <div class="screen__alert-glow"></div>
  <div class="status-bar"></div>

  <div class="location">
    <svg class="location__pin" viewBox="0 0 14 20"><path d="M7 0a7 7 0 0 1 7 7c0 5-7 13-7 13S0 12 0 7a7 7 0 0 1 7-7z" fill="#fff"/><circle cx="7" cy="7" r="2.6" fill="#d9383a"/></svg>
    <span class="location__road">Al Noor Coastal Road</span>
    <span class="location__community">Community Name</span>
  </div>

  <div class="limits">
    <div class="limit limit--speed">
      <svg class="limit__icon" viewBox="0 0 20 20" fill="none" stroke="#fff" stroke-width="1.3"><path d="M2 15a8 8 0 1 1 16 0z"/><path d="M10 14l4-5"/></svg>
      <span class="limit__value">120</span><span class="limit__unit">Km/h</span>
    </div>
    <div class="limit limit--camera">
      <svg class="limit__icon" viewBox="0 0 20 20" fill="none" stroke="#fff" stroke-width="1.3"><rect x="3" y="2" width="14" height="9"/><circle cx="10" cy="6.5" r="2.5"/><path d="M10 11v8M10 13l-5 6M10 13l5 6"/></svg>
      <span class="limit__value">220</span><span class="limit__unit">m</span>
    </div>
  </div>
  <div class="rule rule--top"></div>

  <svg class="gauge" viewBox="0 0 260 260" fill="none">
    <path d="M43.7 216.3 A122 122 0 1 1 216.3 216.3" stroke="var(--ring)" stroke-width="1.2"/>
    <path d="M56.5 203.5 A104 104 0 1 1 234 130" stroke="var(--tick-on)" stroke-width="16" stroke-dasharray="1.4 2.3"/>
    <path d="M234 130 A104 104 0 0 1 203.5 203.5" stroke="var(--tick-dim)" stroke-width="16" stroke-dasharray="1.4 2.3"/>
    <path d="M130 130 L220 126" stroke="var(--tick-on)" stroke-width="2.4"/>
  </svg>
  <div class="gauge__readout"><span class="gauge__value">140</span><span class="gauge__unit">Km/h</span></div>
  <div class="current-speed">Current Speed</div>

  <div class="rule rule--bottom"></div>
  <nav class="actions">
    <div class="action action--school"><div class="action__icon"><svg viewBox="0 0 16 16" fill="none" stroke="#fff" stroke-width="1"><path d="M1 6l7-3 7 3-7 3z"/><path d="M4 7.5v4l4 2 4-2v-4"/></svg></div><span class="action__label">School Intimation</span></div>
    <div class="action action--report"><div class="action__icon"><svg viewBox="0 0 16 16" fill="none" stroke="#fff" stroke-width="1"><rect x="2" y="2" width="12" height="9"/><circle cx="8" cy="6.5" r="2"/><path d="M6 14h4M8 11v3"/></svg></div><span class="action__label">Report Camera</span></div>
    <div class="action action--settings"><div class="action__icon"><svg viewBox="0 0 16 16" fill="none" stroke="#fff"><circle cx="8" cy="8" r="5.5" stroke-width="2.4" stroke-dasharray="2 2.3"/><circle cx="8" cy="8" r="2.3" stroke-width="1"/></svg></div><span class="action__label">Settings</span></div>
    <div class="action action--exit"><div class="action__icon"><svg viewBox="0 0 16 16" stroke="#fff" stroke-width="1.3"><path d="M3 3l10 10M13 3L3 13"/></svg></div><span class="action__label">Exit</span></div>
  </nav>
</section>

</body>
</html>
```